Website for Fashion/Jewelry online seller

We would like a website design that can be used in wordpress. It will be important to be able to link instagram, twitter, etc posts on the bottom of site. We are to be a online seller of chic jewelry, art, fashion, and other home design industries. Currently we emphasize jewelry but as the years move forward, other products will be introduced as collections in home furnishings and primarily women's fashion. It will be important to have a “shop now” section where people can order products online so ecommerce will need to be set up at some point. The website should have the following feel: clean, modern, contemporary and chic. A lot of whites should be used with simple text and simple but elegant fonts. Best is to go to mirevantello.com to get the best idea of what we are wanting for the look and feel of the site.

Target Market(s)

upper social class people that are into fashion, jewelry, etc

Industry/Entity Type

Fashion

Number of Pages Required

5+ page

Font styles to use
Other font styles liked:
• go to daskorvin.com to see the font desired

Requirements
Must have
• Name of Company is Tide Hollow 7
Nice to have
• see project description
Should not have
• see project description

```html
<!DOCTYPE html>
<html lang="en">
<head>
<meta charset="utf-8">
<title>Tide Hollow 7 — Shop</title>
<link rel="stylesheet" href="https://fonts.googleapis.com/css2?family=Cinzel:wght@400;500&display=swap">
<style>
  :root {
    --ink: #4a4a4a;
    --ink-soft: #6b6b6b;
    --rule: #9a9a9a;
    --active: #c2c2c2;
    --footer: #555555;
    --footer-ink: #e8e8e8;
    --paper: #ffffff;
  }
  * { box-sizing: border-box; margin: 0; padding: 0; }
  html, body { width: 1200px; height: 932px; overflow: hidden; background: var(--paper); }
  body { position: relative; font-family: "Cinzel", serif; color: var(--ink); }

  .brand { position: absolute; left: 92px; top: 18px; font-size: 31px; font-weight: 400; letter-spacing: 1px; color: var(--ink-soft); }

  .main-nav { position: absolute; top: 30px; right: 0; left: 0; }
  .main-nav a { position: absolute; top: 0; height: 22px; line-height: 22px; font-size: 11px; letter-spacing: .6px; color: var(--ink); text-decoration: none; text-transform: uppercase; }
  .main-nav a.is-active { background: var(--active); color: #fff; padding: 0 14px; }
  .nav-home { left: 601px; } .nav-shop { left: 654px; } .nav-about { left: 729px; }
  .nav-charity { left: 796px; } .nav-locations { left: 877px; } .nav-contact { left: 972px; }

  .icon-search { position: absolute; left: 1044px; top: 33px; }
  .icon-cart { position: absolute; left: 1073px; top: 18px; }

  .sidebar { position: absolute; left: 95px; top: 81px; width: 238px; }
  .sidebar-title { border-top: 1px solid var(--rule); border-bottom: 1px solid var(--rule); height: 40px; line-height: 38px; font-size: 12.5px; color: var(--ink-soft); }
  .sidebar-list { list-style: none; margin-top: 25px; }
  .sidebar-list li { font-size: 10.5px; height: 28.8px; letter-spacing: .3px; }

  .product-grid { position: absolute; left: 350px; top: 81px; display: grid; grid-template-columns: repeat(3, 237px); grid-template-rows: repeat(2, 343px); column-gap: 19px; row-gap: 19px; }
  .product { position: relative; }
  .product-image { width: 100%; height: 100%; }
  .product-info { position: absolute; left: 0; right: 0; bottom: 0; height: 62px; background: rgba(240,240,240,.85); text-align: center; padding-top: 14px; }
  .product-name { font-size: 10px; letter-spacing: .4px; }
  .product-price { font-size: 15px; margin-top: 2px; }

  .site-footer { position: absolute; left: 0; top: 885px; width: 1200px; height: 47px; background: var(--footer); color: var(--footer-ink); }
  .copyright { position: absolute; left: 95px; top: 17px; font-size: 9.5px; letter-spacing: .3px; }
  .social { position: absolute; right: 99px; top: 13px; display: flex; gap: 3px; }
  .social span { width: 19px; height: 19px; border: 1px solid var(--footer-ink); border-radius: 50%; }
</style>
</head>
<body>
  <div class="brand">Tide Hollow 7</div>

  <nav class="main-nav">
    <a class="nav-home">Home</a>
    <a class="nav-shop is-active">Shop</a>
    <a class="nav-about">About</a>
    <a class="nav-charity">Charity</a>
    <a class="nav-locations">Locations</a>
    <a class="nav-contact">Contact</a>
  </nav>

  <svg class="icon-search" width="16" height="16" viewBox="0 0 16 16" aria-label="Search">
    <circle cx="7" cy="7" r="5.5" fill="none" stroke="#aaa" stroke-width="1.2"/>
    <line x1="11" y1="11" x2="15" y2="15" stroke="#aaa" stroke-width="1.2"/>
  </svg>
  <svg class="icon-cart" width="30" height="32" viewBox="0 0 30 32" aria-label="Cart, 0 items">
    <circle cx="18" cy="10" r="8" fill="#fff" stroke="#666" stroke-width="1"/>
    <text x="18" y="14" text-anchor="middle" font-family="Cinzel, serif" font-size="10" fill="#444">0</text>
    <path d="M2 19h2l2 8h8l2-6H5" fill="none" stroke="#aaa" stroke-width="1.1"/>
    <circle cx="7.5" cy="29.5" r="1" fill="#aaa"/><circle cx="12.5" cy="29.5" r="1" fill="#aaa"/>
  </svg>

  <aside class="sidebar">
    <h2 class="sidebar-title">Shop</h2>
    <ul class="sidebar-list">
      <li>New Arrivals</li><li>Pre Order</li><li>All</li><li>Dresses</li><li>Tops</li>
      <li>Skirts</li><li>Pants</li><li>Knitwear</li><li>Coats &amp; Jackets</li><li>Shoes</li><li>Sale</li>
    </ul>
  </aside>

  <main class="product-grid">
    <div class="product"><div class="product-image" role="img" aria-label="Turquoise and grey beaded necklaces with silver medals on a wooden slab" style="background:linear-gradient(160deg,#8a8d8c,#6e5a45 55%,#4e3a28)"></div></div>
    <div class="product">
      <div class="product-image" role="img" aria-label="Turquoise and black beaded necklace over watercolour postcards" style="background:linear-gradient(160deg,#d9d6cf,#a9c3c2 50%,#c9c3bb)"></div>
      <div class="product-info"><p class="product-name">Name of Product</p><p class="product-price">$22.00</p></div>
    </div>
    <div class="product"><div class="product-image" role="img" aria-label="Metallic leather cuffs with druzy stone buttons" style="background:linear-gradient(170deg,#c8ccce,#8a6a5c 40%,#6e6a6a 75%,#c0c4c6)"></div></div>
    <div class="product"><div class="product-image" role="img" aria-label="Grey braided leather wrap bracelet with gold chain and pyrite beads" style="background:linear-gradient(170deg,#d8d2c8,#7e8088 50%,#cfc8bc)"></div></div>
    <div class="product"><div class="product-image" role="img" aria-label="Turquoise braided leather wrap bracelet with gold chain and beads" style="background:linear-gradient(170deg,#d8d2c8,#2f8fae 45%,#2a7f9c 70%,#d2cbc0)"></div></div>
    <div class="product"><div class="product-image" role="img" aria-label="Yellow roses and lilies in a glass vase on a tree stump side table" style="background:linear-gradient(180deg,#e9e3d4,#c9b88a 30%,#7a5238 60%,#5a3e2c)"></div></div>
  </main>

  <footer class="site-footer">
    <p class="copyright">© All Right Reserved 2016, TIDEHOLLOW 7</p>
    <div class="social" aria-label="Social links"><span></span><span></span><span></span><span></span></div>
  </footer>
</body>
</html>
```